Healthcare website - Diabetic Shoes - Vitacor - No Cost

I am looking to upgrade my website. I do not want to use Wordpress, Adobe Muse or another designing program. The code should be easily editable using textpad or VI. After the project is done I want to easily add my custom PHP code.

Features
Creative and Modern Design .
Fully responsive site for use on mobile devices
bootstrap, jquery

My current website is
www.stridewellfeet.com

Target Market(s)

Older people who have diabetes. Target market is +60 years old, but we do have younger people going to the site to help out their parents.

Industry/Entity Type

Healthcare

Coding

Coded - Design and coding required

Number of Pages Required

2 page

Colors

Designer to choose colors to be used in the design.

Requirements
Must have
• The code should be easily editable using textpad or VI. After the project is done I want to easily add my custom PHP code.
• The first page will be the home page and the other page I need is this form.
• https://www.stridewellfeet.com/stride-well-feet-do-i-qualify.php
Should not have
• I do not want to use Wordpress, Adobe Muse or another designing program.

```html
<!DOCTYPE html>
<html lang="en">
<head>
<meta charset="utf-8">
<title>StrideWell Feet – Do I Qualify?</title>
<link href="https://fonts.googleapis.com/css2?family=Fredoka:wght@400;500&family=Lato:wght@400;700&display=swap" rel="stylesheet">
<style>
:root{
  --blue:#4a7aa3;
  --blue-dark:#3d6f96;
  --green:#62bb55;
  --text:#333;
  --muted:#8a8a8a;
  --line:#cfcfcf;
  --panel:#efefef;
  --white:#fff;
}
*{box-sizing:border-box;margin:0;padding:0}
html,body{width:900px;height:1200px;overflow:hidden;background:var(--white);font-family:"Lato",sans-serif;color:var(--text)}
.page{position:relative;width:900px;height:1200px}
.abs{position:absolute}

/* top bar */
.topbar{left:0;top:0;width:900px;height:27px;background:var(--blue)}
.social{display:flex;gap:6px}
.social span{width:19px;height:19px;border:1.5px solid var(--white);border-radius:50%;display:block}
.topbar .social{position:absolute;left:74px;top:4px}
.top-btn{position:absolute;top:0;height:27px;background:var(--green);color:var(--white);font-size:11.5px;display:flex;align-items:center;justify-content:center;gap:5px;white-space:nowrap}
.top-btn.login{left:670px;width:70px}
.top-btn.chat{left:743px;width:83px}

/* header */
.brand{left:74px;top:44px;font-family:"Fredoka",sans-serif;font-weight:500;font-size:29px;color:var(--blue);letter-spacing:-0.5px;display:flex;align-items:center;gap:6px}
.brand i{width:12px;height:12px;border-radius:50%;background:var(--green);display:block}
.contact{display:flex;align-items:center;gap:9px;top:46px}
.contact .ring{width:29px;height:29px;border:1.5px solid var(--blue);border-radius:50%;display:flex;align-items:center;justify-content:center}
.contact small{display:block;font-size:9px;color:var(--blue)}
.contact b{display:block;font-weight:400;font-size:12px;color:var(--text);margin-top:2px}
.contact.phone{left:515px}
.contact.mail{left:671px}

/* nav */
.rule{left:0;top:97px;width:900px;height:2px;background:var(--blue)}
.nav{left:74px;top:98px;width:752px;height:33px;background:var(--blue);clip-path:polygon(0 0,100% 0,98.8% 100%,1.2% 100%)}
.nav ul{list-style:none;display:flex;justify-content:center;height:100%;align-items:center;font-family:"Fredoka",sans-serif;font-size:13.5px;color:var(--white);white-space:nowrap}
.nav li{padding:0 13px;border-left:1px solid rgba(255,255,255,.35);line-height:18px;position:relative}
.nav li:first-child{border-left:0}
.nav li.active::after{content:"";position:absolute;left:13px;right:13px;bottom:-8px;height:2px;background:var(--green)}

/* intro */
.title{left:0;top:168px;width:900px;text-align:center;font-family:"Fredoka",sans-serif;font-weight:500;font-size:25px;color:var(--blue-dark)}
.title em{font-style:normal;color:var(--green)}
.intro{left:84px;top:218px;width:732px;text-align:center;font-size:10.3px;line-height:17.5px}
.intro p+p{margin-top:8px}

/* form panels */
.panel{left:74px;width:752px;border:1px solid var(--line);background:var(--white)}
.panel-head{margin:2px;height:32px;background:var(--panel);display:flex;align-items:center;justify-content:space-between;padding:0 12px;font-family:"Fredoka",sans-serif;font-size:12.5px;color:#555}
.panel-head.open{background:var(--green);color:var(--white)}
.toggle{display:block;width:12px;height:12px}
.fields{display:grid;grid-template-columns:repeat(3,235px);column-gap:11px;row-gap:15px;padding:16px 11px 0}
.field{height:32px;border:1px solid var(--line);font-size:9.5px;color:var(--muted);padding:0 8px;display:flex;align-items:center;justify-content:space-between}

.consent{left:84px;top:811px;width:732px;text-align:center;font-size:10.5px;line-height:18.5px}
.submit{left:390px;top:860px;width:119px;height:35px;background:var(--green);color:var(--white);font-weight:700;font-size:16px;display:flex;align-items:center;justify-content:center}

/* footer */
.footer{left:0;top:934px;width:900px;height:234px;background:var(--blue);color:var(--white)}
.fcol{position:absolute;top:26px}
.fcol h4{font-family:"Fredoka",sans-serif;font-weight:500;font-size:12.5px;padding-bottom:10px;border-bottom:1px solid rgba(255,255,255,.35)}
.links{list-style:none;margin-top:10px;font-size:9.5px}
.links li{height:21.2px;display:flex;align-items:center;gap:6px;white-space:nowrap}
.links li::before{content:"";width:3px;height:3px;border-radius:50%;background:var(--white)}
.addr{font-size:9.7px;line-height:16px;margin-top:10px}
.crow{display:flex;align-items:center;gap:9px;font-size:9.7px;margin-top:16px}
.map{position:absolute;left:1px;top:50px;width:193px;height:134px;border:3px solid #7c9cbb;background:linear-gradient(90deg,#dfe3d8 0%,#e6e3d6 55%,#a8c8ea 75%,#8fbbe8 100%)}
.vdiv{position:absolute;top:46px;width:1px;height:150px;background:rgba(255,255,255,.25)}
.fbrand{position:absolute;left:692px;top:72px;font-family:"Fredoka",sans-serif;font-weight:500;font-size:19px;color:var(--white)}
.badges{position:absolute;left:696px;top:114px;width:127px;height:70px;background:var(--white);display:flex;align-items:center;justify-content:space-around}
.badges .b1{width:36px;height:46px;background:#2e7d5b}
.badges .b2{width:48px;height:24px;border-top:3px solid #222;border-bottom:3px solid #222}

.bottombar{left:0;top:1168px;width:900px;height:32px;background:var(--green);color:var(--white);font-size:9.5px;display:flex;align-items:center;padding:0 75px;justify-content:space-between}
.bottombar .social span{width:20px;height:20px}
</style>
</head>
<body>
<div class="page">

  <div class="abs topbar">
    <div class="social"><span></span><span></span><span></span><span></span></div>
    <div class="top-btn login">
      <svg width="11" height="12" viewBox="0 0 11 12"><rect x="1" y="5" width="9" height="7" rx="1" fill="#fff"/><path d="M3 5V3.5a2.5 2.5 0 0 1 5 0V5" stroke="#fff" stroke-width="1.5" fill="none"/></svg>
      Login
    </div>
    <div class="top-btn chat">
      <svg width="13" height="13" viewBox="0 0 13 13"><circle cx="6.5" cy="4.5" r="3" fill="none" stroke="#fff" stroke-width="1.4"/><path d="M1.5 12.5c.5-3 2.5-4.5 5-4.5s4.5 1.5 5 4.5" fill="none" stroke="#fff" stroke-width="1.4"/></svg>
      Live Chat
    </div>
  </div>

  <div class="abs brand"><i></i>stridewell feet</div>

  <div class="abs contact phone">
    <div class="ring"><svg width="13" height="13" viewBox="0 0 24 24"><path d="M6.6 10.8a15 15 0 0 0 6.6 6.6l2.2-2.2c.3-.3.7-.4 1-.2 1.1.4 2.3.6 3.6.6.6 0 1 .4 1 1V20c0 .6-.4 1-1 1A17 17 0 0 1 3 4c0-.6.4-1 1-1h3.5c.6 0 1 .4 1 1 0 1.3.2 2.5.6 3.6.1.3 0 .7-.2 1z" fill="#62bb55"/></svg></div>
    <div><small>Phone:</small><b>1-800-555-0142</b></div>
  </div>
  <div class="abs contact mail">
    <div class="ring"><svg width="13" height="11" viewBox="0 0 13 11"><rect x=".75" y=".75" width="11.5" height="9.5" rx="1" fill="none" stroke="#62bb55" stroke-width="1.3"/><path d="M1 1.5l5.5 4.5L12 1.5" fill="none" stroke="#62bb55" stroke-width="1.3"/></svg></div>
    <div><small>Email:</small><b>info@stridewellfeet.com</b></div>
  </div>

  <div class="abs rule"></div>
  <nav class="abs nav">
    <ul>
      <li>Home</li>
      <li class="active">StrideWell Feet! Do I Qualify!</li>
      <li>Why Diabetic Shoes?</li>
      <li>Shoes</li>
      <li>Products</li>
      <li>Shoe Fitter Jobs</li>
      <li>FAQ</li>
    </ul>
  </nav>

  <h1 class="abs title">StrideWell Feet <em>Do I Qualify?</em></h1>

  <div class="abs intro">
    <p>You may be eligible for shoes - at no cost to you! Enter your information in the form below to find out if you qualify for shoe coverage. Vitacor or your insurance provider may cover the cost of one pair of shoes and three pairs of custom or heat molded insoles per calendar year. Find out if you qualify now!</p>
    <p>Besides Vitacor, here is a list of private insurance providers: Silverline Health Care, Arbora, Kestrel Shield, VetCare Plus, Covewell, Harbor Shield, Humaris, Bluefen Health, Care Forward, Peakline, Clear Vista Plans, Commonway Health Care, TriServe, Wellridge Care. Any many more.</p>
  </div>

  <section class="abs panel" style="top:329px;height:204px">
    <div class="panel-head open">Personal Information<svg class="toggle" viewBox="0 0 12 12"><path d="M0 6h12" stroke="#fff" stroke-width="2"/></svg></div>
    <div class="fields">
      <div class="field">Your Name:</div>
      <div class="field">Address:</div>
      <div class="field">City:</div>
      <div class="field">State:</div>
      <div class="field">Zip:</div>
      <div class="field">Gender:</div>
      <div class="field">Date of Birth:
        <svg width="16" height="16" viewBox="0 0 16 16"><rect x="1" y="3" width="14" height="12" rx="1" fill="none" stroke="#888" stroke-width="1.3"/><path d="M1 6.5h14M4.5 1v3M11.5 1v3" stroke="#888" stroke-width="1.3"/><g fill="#888"><rect x="3.5" y="8.5" width="2" height="2"/><rect x="7" y="8.5" width="2" height="2"/><rect x="10.5" y="8.5" width="2" height="2"/><rect x="3.5" y="11.5" width="2" height="2"/><rect x="7" y="11.5" width="2" height="2"/></g></svg>
      </div>
      <div class="field">Phone :</div>
    </div>
  </section>

  <section class="abs panel" style="top:559px"><div class="panel-head">Vitacor and Insurance Information<svg class="toggle" viewBox="0 0 12 12"><path d="M0 6h12M6 0v12" stroke="#888" stroke-width="2"/></svg></div></section>
  <section class="abs panel" style="top:608px"><div class="panel-head">Supplementary / Secondary Insurance Information<svg class="toggle" viewBox="0 0 12 12"><path d="M0 6h12M6 0v12" stroke="#888" stroke-width="2"/></svg></div></section>
  <section class="abs panel" style="top:657px"><div class="panel-head">Primary Physician Information (M.D or D.O only No Podiatrist Please)<svg class="toggle" viewBox="0 0 12 12"><path d="M0 6h12M6 0v12" stroke="#888" stroke-width="2"/></svg></div></section>
  <section class="abs panel" style="top:706px"><div class="panel-head">Vitacor Covered Products (Check next to each product you want to receive)<svg class="toggle" viewBox="0 0 12 12"><path d="M0 6h12M6 0v12" stroke="#888" stroke-width="2"/></svg></div></section>
  <section class="abs panel" style="top:755px"><div class="panel-head">Confirm &amp; Submit Application<svg class="toggle" viewBox="0 0 12 12"><path d="M0 6h12M6 0v12" stroke="#888" stroke-width="2"/></svg></div></section>

  <p class="abs consent">By submitting this information, I authorize StrideWellFeet.com/Harborline Medical Supply Inc., its affiliates, subsidiaries, or parent company to contact me by phone or email. Please be assured that we value and protect your privacy. Remember, there is no purchase necessary to see if you qualify.</p>
  <div class="abs submit">Submit</div>

  <footer class="abs footer">
    <div class="fcol" style="left:75px;width:138px">
      <h4>QUICK LINKS</h4>
      <ul class="links">
        <li>Home</li><li>StrideWell Feet! Do I Qualify!</li><li>Why Diabetic Shoes?</li><li>Shoes</li><li>Products</li><li>Shoe Fitter Jobs</li><li>FAQ</li>
      </ul>
    </div>
    <div class="vdiv" style="left:234px"></div>
    <div class="fcol" style="left:259px;width:145px">
      <h4>CONTACT DETAILS</h4>
      <p class="addr">Harborline Medical<br>2400 Meridian Ave Ste 310<br>Lakeview, Fl 33400</p>
      <div class="crow"><svg width="11" height="11" viewBox="0 0 24 24"><path d="M6.6 10.8a15 15 0 0 0 6.6 6.6l2.2-2.2c.3-.3.7-.4 1-.2 1.1.4 2.3.6 3.6.6.6 0 1 .4 1 1V20c0 .6-.4 1-1 1A17 17 0 0 1 3 4c0-.6.4-1 1-1h3.5c.6 0 1 .4 1 1 0 1.3.2 2.5.6 3.6.1.3 0 .7-.2 1z" fill="#fff"/></svg>818-555-0190</div>
      <div class="crow" style="margin-top:22px"><svg width="12" height="11" viewBox="0 0 12 11"><rect x="3" y="0" width="6" height="3" fill="#fff"/><rect x="0" y="3.5" width="12" height="5" rx="1" fill="#fff"/><rect x="3" y="7" width="6" height="4" fill="#fff" stroke="#4a7aa3" stroke-width=".8"/></svg>828.555.0177</div>
      <div class="crow" style="margin-top:22px"><svg width="11" height="9" viewBox="0 0 11 9"><rect width="11" height="9" fill="#fff"/><path d="M0 0l5.5 4.5L11 0" fill="none" stroke="#4a7aa3" stroke-width="1"/></svg>info@stridewellfeet.com</div>
    </div>
    <div class="vdiv" style="left:427px"></div>
    <div class="fcol" style="left:450px;width:198px">
      <h4>LOCATION MAP</h4>
      <div class="map" role="img" aria-label="Street map showing the office location near the coast"></div>
    </div>
    <div class="fbrand">stridewell feet</div>
    <div class="badges" role="img" aria-label="Accreditation and compliance badges"><span class="b1"></span><span class="b2"></span></div>
  </footer>

  <div class="abs bottombar">
    <span>Copyright © 2017 StrideWell Feet. All Rights Reserved &nbsp;|&nbsp; Terms of Use &nbsp;|&nbsp; Privacy Policy &nbsp;|&nbsp; Returns/Exchanges</span>
    <div class="social"><span></span><span></span><span></span><span></span></div>
  </div>

</div>
</body>
</html>
```